New Business Card Design Project

I need a design for business cards, i am an electrical business called "Vantor Electrical and Communications" i need the cards to be double sided with the company logo on the back (attached) the front needs to say my company name, web site, email address, telephone number, and ABN number and electrical license number. I am open to different arrangements of the information but would like the background to be incorporating something electrical or something that looks smart. open to all additional ideas also.

The company colours are orange and grey see logo attached.

Business Name: Vantor Electrical and Communications
Website: vantorelectricalandcomms.example.au
Email: dean@vantorelectricalandcomms.example.au
Telephone(mobile): 0481290736
ABN: 71829304516
Lic No: 483027D

Target Market(s)

Business entities, Project Managers, Accounts, Clients

Industry/Entity Type

Electrician

Contact Information for Business Card

I need a design for business cards, i am an electrical business called "Vantor Electrical and Communications" i need the cards to be double sided with the company logo on the back (attached) the front needs to say my company name

Font styles to use
Serif
Sans Serif

Colors
f37122
5c5c5c

Requirements
Must have
• Must have the Logo on the back open to different ways of it being on the back but had in mind to keep it central but again open to other options
Nice to have
• A real modern cool background that is eye catching yet contemporary
Should not have
• No backgrounds of a light bulb or plug or anything like that

```html
<!DOCTYPE html>
<html lang="en">
<head>
<meta charset="utf-8">
<title>Vantor Electrical and Communications – Business Card</title>
<link rel="stylesheet" href="https://fonts.googleapis.com/css2?family=Source+Sans+3:wght@400;600;700&display=swap">
<style>
  :root {
    --backdrop: #4a3438;
    --amber: #f9b122;
    --amber-soft: #fcd27e;
    --amber-pale: #fff3dc;
    --grey: #5c5c5c;
    --white: #ffffff;
    --text-font: "Source Sans 3", sans-serif;
  }
  * { box-sizing: border-box; margin: 0; padding: 0; }
  html, body {
    width: 1200px; height: 1200px; overflow: hidden;
    background: var(--backdrop);
    font-family: var(--text-font);
  }
  .card {
    position: absolute; left: 228px; width: 744px; height: 422px;
    box-shadow: 0 4px 10px rgba(0,0,0,.35);
    overflow: hidden;
  }
  .card--back { top: 146px; }
  .card--front { top: 632px; background: var(--white); }

  .back-surface {
    position: absolute; inset: 0;
    background:
      linear-gradient(115deg, rgba(255,255,255,.35) 0%, rgba(255,255,255,0) 30%, rgba(255,255,255,.3) 55%, rgba(255,255,255,0) 80%),
      var(--amber);
  }
  .brand {
    position: absolute; font-weight: 600; line-height: 1; text-transform: uppercase;
  }
  .card--back .brand {
    left: 0; right: 0; top: 140px; text-align: center; color: var(--white);
  }
  .brand__name { display: block; font-size: 96px; letter-spacing: 6px; }
  .brand__tag { display: block; font-size: 26px; letter-spacing: 2px; margin-top: 14px; }

  .front-glow {
    position: absolute; right: 0; top: 0; width: 380px; height: 100%;
    background: linear-gradient(100deg, rgba(255,255,255,0) 0%, var(--amber-pale) 45%, rgba(255,255,255,0) 100%);
  }
  .card--front .brand { left: 50px; top: 92px; color: var(--amber); }
  .card--front .brand__name { font-size: 62px; letter-spacing: 4px; }
  .card--front .brand__tag { font-size: 17px; letter-spacing: 1px; margin-top: 10px; }

  .person { position: absolute; right: 39px; top: 212px; text-align: right; }
  .person__name { font-size: 28px; font-weight: 700; color: var(--amber); line-height: 1.1; }
  .person__role { font-size: 19px; color: var(--grey); margin-top: 2px; }

  .contact { position: absolute; left: 38px; top: 304px; list-style: none; }
  .contact li {
    display: flex; align-items: center; gap: 10px;
    font-size: 19px; color: var(--grey); height: 25px;
  }
  .contact svg { width: 18px; height: 18px; flex: none; }

  .registration {
    position: absolute; right: 39px; top: 330px; text-align: right;
    font-size: 19px; color: var(--grey); line-height: 25px;
  }
  .registration b { font-weight: 700; }

  .front-band { position: absolute; left: 0; bottom: 0; width: 744px; height: 34px; }
</style>
</head>
<body>

<section class="card card--back" aria-label="Card back">
  <div class="back-surface"></div>
  <div class="brand">
    <span class="brand__name">Vantor</span>
    <span class="brand__tag">Electrical &amp; Communications</span>
  </div>
</section>

<section class="card card--front" aria-label="Card front">
  <div class="front-glow"></div>

  <div class="brand">
    <span class="brand__name">Vantor</span>
    <span class="brand__tag">Electrical &amp; Communications</span>
  </div>

  <div class="person">
    <p class="person__name">Marco Ellison</p>
    <p class="person__role">Managing Partner</p>
  </div>

  <ul class="contact">
    <li>
      <svg viewBox="0 0 18 18" aria-hidden="true"><rect x="4" y="1" width="10" height="16" rx="1.5" fill="none" stroke="#f9b122" stroke-width="2"/><circle cx="9" cy="14" r="1" fill="#f9b122"/></svg>
      0481290736
    </li>
    <li>
      <svg viewBox="0 0 18 18" aria-hidden="true"><rect x="1" y="3" width="16" height="12" fill="#f9b122"/><path d="M1 3 L9 10 L17 3 M1 15 L7 9 M17 15 L11 9" stroke="#fff" stroke-width="1.3" fill="none"/></svg>
      dean@vantorelectricalandcomms.example.au
    </li>
    <li>
      <svg viewBox="0 0 18 18" aria-hidden="true"><circle cx="9" cy="9" r="8" fill="#f9b122"/><path d="M1 9 H17 M9 1 V17 M3 5 H15 M3 13 H15" stroke="#fff" stroke-width="1"/><ellipse cx="9" cy="9" rx="4" ry="8" fill="none" stroke="#fff" stroke-width="1"/></svg>
      vantorelectricalandcomms.example.au
    </li>
  </ul>

  <div class="registration">
    <p><b>ABN:</b> 71829304516</p>
    <p><b>Lic No:</b> 483027D</p>
  </div>

  <svg class="front-band" viewBox="0 0 744 34" aria-hidden="true">
    <defs>
      <linearGradient id="bandFill" x1="0" x2="1" y1="0" y2="0">
        <stop offset="0" stop-color="#f9b122"/>
        <stop offset="0.6" stop-color="#fcd27e"/>
        <stop offset="1" stop-color="#fff3dc"/>
      </linearGradient>
    </defs>
    <rect x="0" y="18" width="744" height="16" fill="url(#bandFill)"/>
    <polygon points="456,34 476,0 744,0 744,34" fill="url(#bandFill)"/>
  </svg>
</section>

</body>
</html>
```